1 Page for Computer Repair Website

Looking for a 1 page website with a design that compliments the business card and pamphlet that have already been made (attached files). It should look business professional and easy to read. Email and phone number should be somewhere near the top of the website, visible when the page loads. I don't want any forms for people to mess with. No "Contact Us" form or entering in email for newsletter. Customers will just be looking at this site to confirm we are professionals and have our business in order.

Target Market(s)

Home and small business

Industry/Entity Type

Computer Repair

Coding

Coded - Design and coding required

Number of Pages Required

1 page

Font styles to use
Other font styles liked:
• Helvetica variations used in pamphlet and card

Colors
0455a3
cfdeed
85abd2
3276b5
85cae6
ffffff

Requirements
Must have
• Compliment the pamphlet and business card in color choices and font use. Pleasing to the eye and easy to read through categories and text.
Should not have
• Forms. No "enter name and email here" or anything of the sort.

```html
<!DOCTYPE html>
<html lang="en">
<head>
<meta charset="utf-8">
<title>PCMEND – Computer Repair</title>
<link href="https://fonts.googleapis.com/css2?family=Arimo:wght@400;700&display=swap" rel="stylesheet">
<style>
:root{
  --blue:#0455a3;
  --blue-mid:#3276b5;
  --blue-soft:#85abd2;
  --blue-sky:#85cae6;
  --blue-pale:#cfdeed;
  --white:#ffffff;
  --ink:#2b2f36;
  --grey:#7a808a;
  --line:#d7dce3;
  --panel:#f2f4f7;
  --foot:#3b3d40;
  --foot-dark:#2a2b2d;
}
*{margin:0;padding:0;box-sizing:border-box}
html,body{width:1200px;height:3220px;overflow:hidden}
body{font-family:"Arimo",Helvetica,Arial,sans-serif;color:var(--ink);background:var(--white);position:relative}
.abs{position:absolute}

/* header */
.site-header{position:absolute;left:0;top:0;width:1200px;height:88px;background:var(--white);border-bottom:1px solid var(--line)}
.brand{position:absolute;left:48px;top:26px;display:flex;align-items:center;gap:10px;font-size:28px;font-weight:700;color:var(--blue)}
.brand-mark{width:14px;height:14px;background:var(--blue)}
.main-nav{position:absolute;left:360px;top:30px;display:flex;gap:10px}
.main-nav a{font-size:12px;font-weight:700;color:var(--ink);text-decoration:none;padding:8px 14px;letter-spacing:.5px}
.main-nav a.active{border:1px solid var(--blue);color:var(--blue)}
.call-btn{position:absolute;right:40px;top:28px;background:var(--blue);color:var(--white);font-size:12px;font-weight:700;padding:10px 16px;display:flex;gap:8px;align-items:center}
.contact-strip{position:absolute;right:40px;top:66px;font-size:11px;color:var(--grey)}

/* hero */
.hero{position:absolute;left:0;top:88px;width:1200px;height:540px;background:linear-gradient(180deg,#f4f7fb,#e7eef6)}
.hero-photo{position:absolute;right:0;top:0;width:620px;height:480px;background:linear-gradient(135deg,#dfe8f1 0%,#b9cde0 45%,#6f8fb0 100%)}
.hero-title{position:absolute;left:90px;top:110px;font-size:42px;line-height:50px;font-weight:700;color:var(--ink)}
.hero-title span{color:var(--blue)}
.hero-lead{position:absolute;left:90px;top:230px;width:430px;background:var(--blue);color:var(--white);font-size:14px;line-height:22px;padding:14px 18px}
.hero-btn{position:absolute;left:90px;top:340px;background:var(--blue-mid);color:var(--white);font-size:13px;font-weight:700;padding:12px 20px}
.hero-curve{position:absolute;left:0;top:520px}

/* section headings */
.sec-title{position:absolute;left:0;width:1200px;text-align:center;font-size:34px;font-weight:700;color:var(--blue)}
.sec-sub{position:absolute;left:0;width:1200px;text-align:center;font-size:16px;color:var(--grey);line-height:24px}

/* photo placeholders */
.photo{position:absolute;background:linear-gradient(135deg,#e3eaf2 0%,#a9bed2 55%,#62809f 100%)}

/* about */
.about-rail{position:absolute;left:600px;top:780px;width:2px;height:380px;background:var(--line)}
.rail-dot{position:absolute;left:594px;width:14px;height:14px;border-radius:50%;background:var(--white);border:3px solid var(--blue)}
.about-copy{position:absolute;left:640px;top:810px;width:380px}
.about-copy .lead{font-size:17px;line-height:25px;color:var(--ink)}
.about-copy .body{font-size:12px;line-height:19px;color:var(--grey);margin-top:14px}
.point-list{list-style:none;margin-top:18px}
.point-list li{display:flex;align-items:center;gap:12px;font-size:13px;margin-bottom:12px;color:var(--ink)}
.point-list li.on{color:var(--blue);font-weight:700}
.num{width:22px;height:22px;border-radius:50%;background:#23262b;color:var(--white);font-size:11px;display:flex;align-items:center;justify-content:center;font-weight:700;flex:none}
.on .num{background:var(--blue)}
.about-link{font-size:12px;color:var(--blue);margin-top:8px}

/* services */
.services{position:absolute;left:0;top:1190px;width:1200px;height:1010px;background:var(--panel)}
.service{position:absolute;width:260px;text-align:center}
.service-icon{width:64px;height:64px;border-radius:50%;background:var(--white);border:1px solid var(--line);margin:0 auto;display:flex;align-items:center;justify-content:center}
.service-icon.lit{background:var(--blue);border-color:var(--blue)}
.service h3{font-size:15px;font-weight:700;margin-top:18px}
.service p{font-size:12px;line-height:19px;color:var(--grey);margin-top:10px}
.read-btn{display:inline-block;margin-top:16px;border:1px solid #9aa1ab;font-size:11px;font-weight:700;padding:9px 18px;color:var(--ink);background:var(--white)}
.pager{position:absolute;left:0;top:2130px;width:1200px;display:flex;justify-content:center;gap:8px}
.pager i{width:9px;height:9px;border-radius:50%;background:var(--blue-soft)}
.pager i.on{background:var(--blue)}

/* why */
.feature{position:absolute;width:220px}
.feature.right{text-align:right}
.feature-icon{width:44px;height:44px;border:1px solid var(--line);display:flex;align-items:center;justify-content:center;background:var(--white)}
.feature.right .feature-icon{margin-left:auto}
.feature h4{font-size:15px;color:var(--blue);margin-top:12px}
.feature p{font-size:12px;line-height:19px;color:var(--grey);margin-top:8px}
.learn-btn{position:absolute;left:545px;top:2700px;width:110px;text-align:center;border:1px solid #9aa1ab;font-size:11px;font-weight:700;padding:10px 0}

/* footer */
.site-footer{position:absolute;left:0;top:2800px;width:1200px;height:370px;background:var(--foot);color:#c4c7cc}
.foot-col{position:absolute;top:50px;width:230px}
.foot-col h5{font-size:14px;color:var(--white);letter-spacing:.5px;padding-bottom:12px;border-bottom:1px solid #55585c;margin-bottom:16px}
.foot-col p{font-size:12px;line-height:20px}
.foot-col ul{list-style:none}
.foot-col li{font-size:12px;line-height:26px}
.socials{display:flex;gap:8px;margin-top:16px}
.socials i{width:22px;height:22px;border-radius:50%;border:1px solid #8a8e94}
.foot-bar{position:absolute;left:0;top:3170px;width:1200px;height:50px;background:var(--foot-dark);color:#9a9ea4;font-size:11px}
.foot-bar .copy{position:absolute;left:48px;top:19px}
.foot-bar .legal{position:absolute;right:48px;top:19px;display:flex;gap:24px}
</style>
</head>
<body>

<header class="site-header">
  <div class="brand"><span class="brand-mark"></span>PCMEND</div>
  <nav class="main-nav">
    <a class="active">HOME</a><a>ABOUT</a><a>SERVICES</a><a>WHY CHOOSE US</a><a>CONTACT US</a>
  </nav>
  <div class="call-btn">
    <svg width="12" height="12" viewBox="0 0 24 24"><path fill="#fff" d="M6.6 10.8a15 15 0 006.6 6.6l2.2-2.2c.3-.3.7-.4 1-.2 1.1.4 2.3.6 3.6.6.6 0 1 .4 1 1V20c0 .6-.4 1-1 1A17 17 0 013 4c0-.6.4-1 1-1h3.5c.6 0 1 .4 1 1 0 1.3.2 2.5.6 3.6.1.3 0 .7-.2 1z"/></svg>
    (555) 014-2290
  </div>
  <div class="contact-strip">help@pcmend.example</div>
</header>

<section class="hero">
  <div class="hero-photo" role="img" aria-label="Technician in glasses repairing an open desktop computer"></div>
  <h1 class="hero-title">Protect Your Computer System<br>Across <span>PCMEND</span> Service.</h1>
  <p class="hero-lead">It is a long established fact that a reader will be distracted by the readable content of a page when looking at its layout the point of using.</p>
  <div class="hero-btn">Try it out for services ›</div>
</section>
<svg class="hero-curve" width="1200" height="110" viewBox="0 0 1200 110">
  <path d="M0 40 Q600 120 1200 20 L1200 0 L0 0 Z" fill="#e7eef6"/>
  <path d="M0 40 Q600 120 1200 20" fill="none" stroke="#0455a3" stroke-width="6"/>
  <path d="M0 52 Q600 128 1200 32" fill="none" stroke="#85cae6" stroke-width="2"/>
  <circle cx="600" cy="86" r="8" fill="#fff" stroke="#0455a3" stroke-width="3"/>
</svg>

<h2 class="sec-title" style="top:700px">KNOW ABOUT PCMEND</h2>
<p class="sec-sub" style="top:744px">Your Next Strategic Place</p>
<div class="photo" style="left:150px;top:800px;width:420px;height:275px" role="img" aria-label="Laptop showing a technician at work on a desktop computer"></div>
<div class="about-rail"></div>
<span class="rail-dot" style="top:800px"></span>
<span class="rail-dot" style="top:1140px"></span>
<div class="about-copy">
  <p class="lead">It is a long established fact that a reader will be distracted by the readable content of a page when looking at its layout.</p>
  <p class="body">It is a long established fact that a reader will be distracted by the readable content of a page when looking at its layout. The point of using sample text is that it has a more-or-less normal distribution of letters, as opposed to using content here.</p>
  <ul class="point-list">
    <li class="on"><span class="num">1</span>It is a long established fact that a reader</li>
    <li><span class="num">2</span>Tracked by the readable content of a page when</li>
    <li><span class="num">3</span>Looking at its layout the point of sample text.</li>
  </ul>
  <p class="about-link">Learn more about us and our repair standards »</p>
</div>

<section class="services">
  <h2 class="sec-title" style="top:60px">OUR SERVICE</h2>
  <p class="sec-sub" style="top:108px">It is a long established fact that a reader will be distracted by the<br>readable content of a page when looking at its layout.</p>

  <div class="service" style="left:170px;top:230px">
    <div class="service-icon lit"><svg width="28" height="28" viewBox="0 0 24 24"><path d="M14 3a5 5 0 00-4.6 6.9L3 16.3 5.7 19l6.4-6.4A5 5 0 0019 8l-3 3-3-1-1-3 3-3z" fill="#fff"/></svg></div>
    <h3>Malware Removal</h3>
    <p>It was a distinctly of over 200 safe words, combined with a handful of model sentence structures, to generate text.</p>
    <span class="read-btn">READ MORE</span>
  </div>
  <div class="service" style="left:470px;top:230px">
    <div class="service-icon"><svg width="28" height="28" viewBox="0 0 24 24" fill="none" stroke="#2b2f36" stroke-width="1.6"><rect x="4" y="5" width="16" height="11"/><path d="M2 19h20"/></svg></div>
    <h3>PC / Laptop Hardware Repair</h3>
    <p>It was a distinctly of over 200 safe words, combined with a handful of model sentence structures, to generate text.</p>
    <span class="read-btn">READ MORE</span>
  </div>
  <div class="service" style="left:770px;top:230px">
    <div class="service-icon"><svg width="28" height="28" viewBox="0 0 24 24" fill="none" stroke="#2b2f36" stroke-width="1.6"><ellipse cx="12" cy="6" rx="7" ry="3"/><path d="M5 6v12c0 1.7 3.1 3 7 3s7-1.3 7-3V6M5 12c0 1.7 3.1 3 7 3s7-1.3 7-3"/></svg></div>
    <h3>Hard/Software Upgrades</h3>
    <p>It was a distinctly of over 200 safe words, combined with a handful of model sentence structures, to generate text.</p>
    <span class="read-btn">READ MORE</span>
  </div>

  <div class="service" style="left:170px;top:570px">
    <div class="service-icon"><svg width="28" height="28" viewBox="0 0 24 24" fill="none" stroke="#2b2f36" stroke-width="1.6"><path d="M6 3h9l4 4v14H6z"/><path d="M9 12h7M9 16h7"/></svg></div>
    <h3>Data Migration</h3>
    <p>It was a distinctly of over 200 safe words, combined with a handful of model sentence structures, to generate text.</p>
    <span class="read-btn">READ MORE</span>
  </div>
  <div class="service" style="left:470px;top:570px">
    <div class="service-icon"><svg width="28" height="28" viewBox="0 0 24 24" fill="none" stroke="#2b2f36" stroke-width="1.6"><rect x="3" y="4" width="18" height="12"/><path d="M8 20h8M12 16v4M8 10l3 3 5-5"/></svg></div>
    <h3>Clean / Tune Ups</h3>
    <p>It was a distinctly of over 200 safe words, combined with a handful of model sentence structures, to generate text.</p>
    <span class="read-btn">READ MORE</span>
  </div>
  <div class="service" style="left:770px;top:570px">
    <div class="service-icon"><svg width="28" height="28" viewBox="0 0 24 24" fill="none" stroke="#2b2f36" stroke-width="1.6"><ellipse cx="12" cy="6" rx="7" ry="3"/><path d="M5 6v12c0 1.7 3.1 3 7 3s7-1.3 7-3V6"/><path d="M12 10v7M9 14l3 3 3-3"/></svg></div>
    <h3>Data Rescue</h3>
    <p>It was a distinctly of over 200 safe words, combined with a handful of model sentence structures, to generate text.</p>
    <span class="read-btn">READ MORE</span>
  </div>
</section>
<div class="pager"><i></i><i></i><i class="on"></i><i></i></div>

<h2 class="sec-title" style="top:2250px">WHY CHOOSE US</h2>
<p class="sec-sub" style="top:2296px">It is a long established fact that a reader will be distracted by the<br>readable content of a page when looking at its layout.</p>
<div class="photo" style="left:390px;top:2390px;width:420px;height:262px" role="img" aria-label="Laptop showing a computer repair workstation"></div>
<svg class="abs" style="left:0;top:0" width="1200" height="3220" aria-hidden="true">
  <g stroke="#cfdeed" stroke-width="1.5" fill="none">
    <path d="M320 2410 H380 M320 2580 H380 M880 2410 H820 M880 2580 H820"/>
  </g>
</svg>
<div class="feature" style="left:110px;top:2380px">
  <div class="feature-icon"><svg width="22" height="22" viewBox="0 0 24 24" fill="none" stroke="#0455a3" stroke-width="1.6"><rect x="4" y="4" width="16" height="16"/><circle cx="12" cy="12" r="4"/></svg></div>
  <h4>Featured 1</h4>
  <p>It is a long established fact that a reader will be distracted by the readable content page.</p>
</div>
<div class="feature" style="left:110px;top:2550px">
  <div class="feature-icon"><svg width="22" height="22" viewBox="0 0 24 24" fill="none" stroke="#0455a3" stroke-width="1.6"><path d="M12 3l2.6 5.5 6 .8-4.4 4.2 1 6L12 16.7 6.8 19.5l1-6L3.4 9.3l6-.8z"/></svg></div>
  <h4>Featured 4</h4>
  <p>It is a long established fact that a reader will be distracted by the readable content page.</p>
</div>
<div class="feature right" style="left:870px;top:2380px">
  <div class="feature-icon"><svg width="22" height="22" viewBox="0 0 24 24" fill="none" stroke="#0455a3" stroke-width="1.6"><circle cx="12" cy="12" r="8"/><path d="M12 7v5l3 3"/></svg></div>
  <h4>Featured 2</h4>
  <p>It is a long established fact that a reader will be distracted by the readable content page.</p>
</div>
<div class="feature right" style="left:870px;top:2550px">
  <div class="feature-icon"><svg width="22" height="22" viewBox="0 0 24 24" fill="none" stroke="#0455a3" stroke-width="1.6"><path d="M5 12l4 4 10-10"/></svg></div>
  <h4>Featured 3</h4>
  <p>It is a long established fact that a reader will be distracted by the readable content page.</p>
</div>
<div class="learn-btn">LEARN MORE</div>

<footer class="site-footer">
  <div class="foot-col" style="left:48px">
    <h5>ABOUT PCMEND</h5>
    <p>Home and small business computer repair done right, with clear pricing and honest advice on every job.</p>
    <p style="margin-top:12px">Local, certified technicians serving homes and offices across the region since 2009.</p>
    <div class="socials"><i></i><i></i><i></i><i></i><i></i></div>
  </div>
  <div class="foot-col" style="left:340px">
    <h5>QUICK LINKS</h5>
    <ul><li>Home</li><li>About Us</li><li>Services</li><li>Why Choose Us</li><li>Contact Us</li></ul>
  </div>
  <div class="foot-col" style="left:630px">
    <h5>OUR SERVICES</h5>
    <ul><li>Malware Removal</li><li>Hardware &amp; Software Upgrades</li><li>Data Migration</li><li>Clean / Tune Ups</li><li>Data Rescue</li></ul>
  </div>
  <div class="foot-col" style="left:920px">
    <h5>CONTACT US</h5>
    <p>120 Harbor Lane, Suite 4<br>Riverton, ST 00000</p>
    <p style="margin-top:12px">Ph: (555) 014-2290<br>Fax: (555) 014-2291<br>Email: help@pcmend.example</p>
  </div>
</footer>
<div class="foot-bar">
  <span class="copy">Copyright © 2024 PCMEND. All Rights Reserved.</span>
  <span class="legal"><span>Terms and Condition</span><span>Legal Document</span><span>Privacy Policy</span></span>
</div>

</body>
</html>
```